Patent Law

Need to develop a home page for a patent lawyer.

Colors should go with logo, blues...

Company Name- Corvel Tindry, PLLC

Company Overview-

I am an Intellectual Property Lawyer and focus on patents, copyrights, trademarks, & trade secrets. I work with small businesses and start ups in the chemical and biotech industries.

Why Us-

I am small firm that can provide large-firm service at a reasonable price. I also can charge flat-fees for entreprenuers in certain practice areas.

Services-
Intellectual Property
Patents
Copyrights
Trademarks
Trade secrets
Healthcare Compliance
Elder law
Wills
Trusts

Website we like-
http://www.quarnlowtide.example/ - within industry!!
http://www.vopperhask.example/
http://dulbrickovan.example/
http://thefernwoldguides.example/

Target Market(s)

My customers will be small business, specifically small start-up companies in the chemical and biotech arena.

Industry/Entity Type

Trade

Requirements
Must have
• Colors should go with logo, blues...

```html
<!DOCTYPE html>
<html lang="en">
<head>
<meta charset="utf-8">
<title>Corvel Tindry, PLLC – Patent and IP Specialists</title>
<link rel="stylesheet" href="https://fonts.googleapis.com/css2?family=Arvo:wght@700&family=Cinzel:wght@500&family=Exo+2:wght@300;400;600;700&family=Fira+Sans:wght@400;500;600&family=Open+Sans:wght@400;600&display=swap">
<style>
:root{
  --blue:#0b6db4;
  --blue-deep:#0a5fa0;
  --blue-bright:#1b8fd0;
  --ink:#222;
  --navy:#1f3c5a;
  --grey-band:#dedede;
  --grey-field:#cfcfcf;
  --white:#fff;
}
*{box-sizing:border-box;margin:0;padding:0}
html,body{width:1026px;height:1200px;overflow:hidden;background:var(--white)}
body{font-family:"Open Sans",Arial,sans-serif;color:var(--ink)}
.page{position:relative;width:1026px;height:1200px;overflow:hidden}
.abs{position:absolute}

/* header */
.site-header{left:0;top:0;width:1026px;height:110px;background:var(--white)}
.brand{left:18px;top:30px;display:flex;align-items:center;gap:12px;white-space:nowrap}
.brand-dot{width:50px;height:50px;border-radius:50%;background:var(--blue);flex:none}
.brand-name{font-family:"Cinzel",Georgia,serif;font-weight:500;font-size:26px;color:var(--navy);letter-spacing:.3px}
.call{right:245px;top:22px;font-family:"Exo 2",Arial,sans-serif;font-weight:700;font-size:25px;color:var(--navy);white-space:nowrap}
.call b{color:var(--blue)}
.search-field{left:793px;top:26px;width:160px;height:22px;border:1px solid #9aa;background:#fff}
.search-btn{left:957px;top:25px;width:56px;height:24px;background:var(--blue);color:#fff;font:600 10px "Open Sans",Arial,sans-serif;display:flex;align-items:center;justify-content:center}
.main-nav{right:13px;top:67px;display:flex;font-family:"Open Sans",Arial,sans-serif;font-size:14px;font-weight:600;color:#111;white-space:nowrap}
.main-nav span{padding:0 17px;border-left:1.5px solid #222;line-height:20px}
.main-nav span:first-child{border-left:none}
.main-nav span:last-child{padding-right:0}

/* hero */
.hero{left:0;top:110px;width:1026px;height:387px;background:radial-gradient(ellipse 260px 200px at 600px 140px,#e9863c 0%,#a0512d 25%,#3c4a60 55%,transparent 80%),linear-gradient(180deg,#6d8ab4 0%,#40577c 40%,#1b1f28 70%,#0a0a0c 100%)}
.hero-title{left:66px;top:96px;font-family:"Arvo",Georgia,serif;font-weight:700;font-size:36px;line-height:37px;color:#fff}
.hero-text{left:66px;top:180px;font-family:"Fira Sans",Arial,sans-serif;font-weight:600;font-size:19.5px;line-height:23px;color:#fff}
.hero-cta{left:68px;top:249px;width:316px;height:32px;background:var(--blue-bright);color:#fff;font:500 15px "Fira Sans",Arial,sans-serif;padding:7px 9px}

/* welcome */
.welcome{left:0;top:497px;width:1026px;height:113px;background:var(--blue);color:#fff;text-align:center}
.welcome h1{font-family:"Exo 2",Arial,sans-serif;font-weight:300;font-size:34px;margin-top:20px}
.welcome p{font-family:Arial,sans-serif;font-size:11.5px;line-height:16px;width:900px;margin:6px auto 0}

/* cards */
.feature-field{left:0;top:610px;width:1026px;height:400px;background:repeating-linear-gradient(45deg,#d2d2d2 0 2px,#c8c8c8 2px 4px),var(--grey-field)}
.feature-field::after{content:"";position:absolute;inset:0;background:linear-gradient(180deg,transparent 40%,rgba(240,240,240,.95) 100%)}
.card{top:637px;width:257px;height:345px;background:linear-gradient(180deg,#fafafa,#e4e4e4);box-shadow:0 1px 4px rgba(0,0,0,.35)}
.card-photo{width:257px;height:133px}
.card-title{height:36px;background:var(--blue);border-bottom:5px solid var(--blue-deep);color:#fff;font:600 17px "Fira Sans",Arial,sans-serif;padding:8px 9px;letter-spacing:.3px}
.card-body{font-family:"Fira Sans",Arial,sans-serif;font-size:11.5px;line-height:14px;color:#111;padding:16px}
.card-body a{color:var(--blue);font-weight:600;text-decoration:none;display:block;margin-top:12px}
.service-list{list-style:none;padding-left:16px}
.map{width:174px;height:80px;margin:-8px 0 8px 4px;border:1px solid #bbb;background:linear-gradient(135deg,#e9ecd8,#d6e3ee 60%,#a9c8e6)}

/* cta band */
.cta-band{left:0;top:1010px;width:1026px;height:94px;background:var(--grey-band)}
.cta-brand{left:107px;top:1036px;display:flex;align-items:center;gap:10px;white-space:nowrap}
.cta-brand .brand-dot{width:44px;height:44px}
.cta-brand .brand-name{font-size:21px}
.cta-arrow{left:417px;top:1036px}
.help-line{left:503px;top:1030px;font:400 17px "Exo 2",Arial,sans-serif;color:#444;white-space:nowrap}
.help-phone{left:505px;top:1050px;font:700 30px "Exo 2",Arial,sans-serif;color:var(--blue);white-space:nowrap}
.cta-divider{left:745px;top:1025px;width:1px;height:68px;background:#999}
.connect{left:764px;top:1030px;font:400 17px "Exo 2",Arial,sans-serif;color:#444;white-space:nowrap}
.social{left:770px;top:1058px;display:flex;gap:10px}
.social span{width:26px;height:26px;border-radius:3px;background:var(--blue)}
.social span:first-child{background:#9aa6b2}
.social span:last-child{background:#e8842a}

/* footer */
.site-footer{left:0;top:1104px;width:1026px;height:96px;background:var(--blue)}
.foot-nav{left:128px;top:1137px;display:flex;gap:26px;font:500 13px "Fira Sans",Arial,sans-serif;color:#fff}
.copyright{left:128px;top:1159px;font:11px Arial,sans-serif;color:#e3eefa}
.newsletter-title{left:662px;top:1122px;font:400 17px "Exo 2",Arial,sans-serif;color:#fff}
.newsletter-field{left:662px;top:1155px;width:171px;height:24px;background:#fff;font:11px Arial,sans-serif;color:#333;padding:5px 7px}
.newsletter-btn{left:838px;top:1155px;width:56px;height:24px;background:#3a3a3a;color:#fff;font:11px Arial,sans-serif;display:flex;align-items:center;justify-content:center}
</style>
</head>
<body>
<div class="page">

  <header class="site-header abs">
    <div class="brand abs"><span class="brand-dot"></span><span class="brand-name">CORVEL TINDRY, PLLC</span></div>
    <div class="call abs"><b>Call</b> (919) 555-0148</div>
    <div class="search-field abs"></div>
    <div class="search-btn abs">SEARCH</div>
    <nav class="main-nav abs"><span>Home</span><span>Firm Overview</span><span>Why Us</span><span>Services</span><span>Resources</span><span>Contact Us</span></nav>
  </header>

  <section class="hero abs" role="img" aria-label="Glowing light bulb held up against a sunset sky over the sea">
    <h2 class="hero-title abs">Protect your Ideas -<br>Patent and IP Specialists.</h2>
    <p class="hero-text abs">Don’t let others profit from your ideas. Secure your rights with patent protection.<br>Legal services and solutions for you and your business.</p>
    <div class="hero-cta abs">Contact us for a free patent consultation</div>
  </section>

  <section class="welcome abs">
    <h1>Welcome to Corvel Tindry, PLLC</h1>
    <p>A patent provides the owner with a monopoly and the right to exclude others from commercially exploiting by making, using, selling or importing the invention covered by the claims of the patent, for the life of the patent in each country in which the patent is registered.</p>
  </section>

  <div class="feature-field abs"></div>

  <article class="card abs" style="left:112px">
    <div class="card-photo" role="img" aria-label="Team of colleagues working at a laptop in an office" style="background:linear-gradient(135deg,#d9dde3,#b9c2cc 60%,#8f99a5)"></div>
    <div class="card-title">WHY CORVEL TINDRY</div>
    <div class="card-body">I am small firm that can provide large-firm service at a reasonable price. I also can charge flat-fees for entrepreneurs in certain practice areas.<a>Read more</a></div>
  </article>

  <article class="card abs" style="left:393px">
    <div class="card-photo" role="img" aria-label="Pen resting on a printed intellectual property document" style="background:linear-gradient(135deg,#f4f6f8,#c9d8e8 55%,#7fa3c8)"></div>
    <div class="card-title">WHAT WE DO</div>
    <div class="card-body"><ul class="service-list"><li>Intellectual Property</li><li>Patents</li><li>Copyrights</li><li>Trademarks</li><li>Trade secrets</li><li>Healthcare Compliance</li><li>Elder law</li><li>Wills</li><li>Trusts</li></ul></div>
  </article>

  <article class="card abs" style="left:673px">
    <div class="card-photo" role="img" aria-label="Hands holding a phone beside a laptop" style="background:linear-gradient(135deg,#b7b7b7,#e6e6e6 50%,#8a8a8a)"></div>
    <div class="card-title">CONTACT INFO</div>
    <div class="card-body">
      <div class="map" role="img" aria-label="Street map showing the office location"></div>
      <div style="padding-left:4px">Address : 4120 Larkmoor Bend Lane,<br>Raleigh, North Carolina-27614,<br>United States.<br>Phone : (919) 555-0148<br>Email : info@corveltindry.example</div>
    </div>
  </article>

  <section class="cta-band abs"></section>
  <div class="cta-brand abs"><span class="brand-dot"></span><span class="brand-name">CORVEL TINDRY, PLLC</span></div>
  <svg class="cta-arrow abs" width="60" height="42" viewBox="0 0 60 42"><path d="M2 13h32V2l24 19-24 19V29H2z" fill="none" stroke="#8a8a8a" stroke-width="2"/></svg>
  <div class="help-line abs">New Help Planning? Call us!</div>
  <div class="help-phone abs">(919) 555-0148</div>
  <div class="cta-divider abs"></div>
  <div class="connect abs">Connect with us on</div>
  <div class="social abs"><span></span><span></span><span></span><span></span></div>

  <footer class="site-footer abs"></footer>
  <nav class="foot-nav abs"><span>Home</span><span>Firm Overview</span><span>Why Us</span><span>Services</span><span>Resources</span><span>Contact Us</span></nav>
  <div class="copyright abs">Copyright (c)2013 by Corvel Tindry, PLLC.</div>
  <div class="newsletter-title abs">Subscribe to our Newsletter</div>
  <div class="newsletter-field abs">Your Email Address</div>
  <div class="newsletter-btn abs">Submit</div>

</div>
</body>
</html>
```